依頼詳細
先進的で施工品質の高いイメージを与えるような、かっこいいデザインを
よろしくお願いします。
今後も名刺以外の印刷物のデザインも依頼すると思います。
記載項目
<表面>:会社名、役職名、氏名、郵便番号、住所、電話、FAX、携帯、
E-MAIL、URL
個人の所有資格(裏面でも可)

<裏面>:業務内容(表面でも可)
電気設備工事 設計・施工(蒼峰電力委託工事店)
空調設備工事 設計・施工
LED照明設備 設計・施工・販売

裏面の内容は出来れば記載したいのですが、デザイン重視のため、
変更省略してもOKです。
希望イメージ
シンプル 複雑
単色 カラフル
暗い 明るい
日常 高級
遊び心 厳粛
未来的 伝統的
女性的 男性的
希望する色
青系、水色系
納品ファイル
• 高解像度JPG (.jpg)
• イラストレーター形式 (.ai)
補足説明
会社のロゴは添付ファイルの通りです。色は青系ですが決まっていません。会社名の漢字の字体は丸ゴシックを使うことが多いのですが、こちらも特定していません。
締め切りは延長しません。
こちらのコンペに頂いた提案の中から必ず当選者を選定します。
すでに頂いております、ご提案ありがとうございます。
他に良いご提案がございましたら、締め切りまでお待ちしております。
よろしくお願いします。
■ 選んだ理由

弊社が希望しておりました、先進的で施工品質の高いイメージを与えるようなデザインに仕上がっていました。
採用させて頂いてとても満足しています。
今後とも宜しくお願いします。

■ 提案者全員のお礼・コメント

初めてミルタスクで依頼しましたが、こんなにたくさんのデザイナーの方から素晴らしいご提案を頂きまして、有難うございました。
デザインの質の高さと件数に、驚いております。
今回、残念ながら採用させてもらわなかった方々には、製作に当たりまして大変貴重なお時間を割いて頂いて申し訳なく思っております。
今後、封筒のデザイン、会社案内のパンフレット、ホームページのリニューアルなどを考えております。
その際はぜひご参加下さいます様、宜しくお願いします。

```html
<!DOCTYPE html>
<html lang="ja">
<head>
<meta charset="utf-8">
<title>沢井電気株式会社 名刺</title>
<link rel="stylesheet" href="https://fonts.googleapis.com/css2?family=Noto+Sans+JP:wght@400;500;700;900&family=Noto+Serif+JP:wght@400;500&display=swap">
<style>
  :root {
    --blue: #1f5fb8;
    --blue-deep: #174a9a;
    --blue-light: #2f74d0;
    --ink: #333;
    --line: #c9ccd2;
    --paper: #fff;
  }
  * { margin: 0; padding: 0; box-sizing: border-box; }
  html, body { width: 834px; height: 1200px; overflow: hidden; background: var(--paper); }
  body { position: relative; font-family: "Noto Sans JP", sans-serif; color: var(--ink); }

  .card {
    position: absolute; left: 70px; width: 694px; height: 420px;
    background: var(--paper); border: 1px solid var(--line); overflow: hidden;
  }
  .card--front { top: 40px; }
  .card--back { top: 690px; }

  /* front */
  .brand-panel {
    position: absolute; left: 0; top: 0; width: 226px; height: 100%;
    background: linear-gradient(150deg, var(--blue-light) 0%, var(--blue-deep) 100%);
  }
  .panel-mark {
    position: absolute; left: 0; width: 226px; top: 160px;
    display: flex; flex-direction: column; align-items: center; gap: 10px;
    color: #fff; font-weight: 700; font-size: 17px; letter-spacing: 2px;
  }
  .panel-mark .dot { width: 60px; height: 60px; border-radius: 50%; background: #fff; }
  .tagline {
    position: absolute; left: 30px; bottom: 30px; color: #fff;
    font-weight: 700; font-size: 17px; letter-spacing: .5px;
  }
  .company-name {
    position: absolute; left: 266px; top: 58px;
    color: var(--blue); font-weight: 700; font-size: 21px; letter-spacing: 1px;
  }
  .header-rule { position: absolute; left: 226px; right: 0; top: 112px; height: 1px; background: var(--line); }
  .title { position: absolute; left: 266px; top: 160px; font-size: 13px; font-family: "Noto Serif JP", serif; }
  .person-name {
    position: absolute; left: 262px; top: 186px;
    font-family: "Noto Serif JP", serif; font-weight: 500; font-size: 44px; letter-spacing: 10px; color: #222;
  }
  .contact {
    position: absolute; left: 266px; top: 304px;
    font-family: "Noto Serif JP", serif; font-size: 14px; line-height: 22px; color: #444;
  }

  /* back */
  .back-mark {
    position: absolute; left: 0; width: 300px; top: 46px;
    display: flex; flex-direction: column; align-items: center; gap: 14px;
  }
  .back-mark .dot { width: 70px; height: 70px; border-radius: 50%; background: var(--blue); }
  .back-mark .name { color: var(--blue-deep); font-weight: 700; font-size: 16px; }
  .services { position: absolute; left: 362px; top: 44px; color: var(--blue); }
  .services h2 { font-size: 14px; font-weight: 500; margin-bottom: 14px; }
  .services li { list-style: none; font-size: 18px; font-weight: 500; line-height: 26px; margin-bottom: 8px; }
  .services .note { display: block; font-size: 12px; line-height: 18px; }
  .url { position: absolute; left: 362px; top: 343px; color: var(--blue-deep); font-weight: 700; font-size: 15px; }
</style>
</head>
<body>
  <section class="card card--front">
    <div class="brand-panel" role="img" aria-label="青系の幾何学模様の背景"></div>
    <div class="panel-mark"><span class="dot"></span><span>沢井電気</span></div>
    <div class="tagline">SAFETY &amp; QUALITY</div>
    <div class="company-name">沢井電気株式会社</div>
    <div class="header-rule"></div>
    <div class="title">代表取締役社長</div>
    <div class="person-name">沢井拓真</div>
    <div class="contact">
      <p>〒500-0000 岐阜県青葉郡緑川町 1-13-10</p>
      <p>TEL. 0585-00-1234　FAX. 0585-00-5678</p>
      <p>Mobile. 090-0000-0000</p>
      <p>Mail. sawai@sawaidenki.com</p>
    </div>
  </section>

  <section class="card card--back">
    <div class="back-mark"><span class="dot"></span><span class="name">SAWAI ELECTRIC,LTD</span></div>
    <div class="services">
      <h2>業務内容</h2>
      <ul>
        <li>電気設備工事/設計・施工<span class="note">（蒼峰電力委託工事店）</span></li>
        <li>空調設備工事/設計・施工</li>
        <li>LED照明設備/設計・施工・販売</li>
      </ul>
    </div>
    <div class="url">http://sawaidenki.com</div>
  </section>
</body>
</html>
```